Dental Design, very professional and noticable

Tindale Ridge Dental Surgery is based in Pelican Waters. We are a fast growing dental surgery and are looking for some professional business cards to send to patients.
We would like to see a design that is Vertical and uses the colours Soft Blue, Silver, White and Black. Maybe a full blue side with moto and details on back? Any other ideas or colours that you may think will make the card look unique is fine.
We need all details on the card that are listed above

Target Market(s)

Families, Retired, Other Professionals and Businesses

Industry/Entity Type

Dental

Contact Information for Business Card

Tindale Ridge Dental Surgery
Family, Cosmetic, Preventative
Dr. Owen Castrey
Dental Surgeon
BDS (Adel) FAE FADI FICD FPFA
phone: (07)50001846
fax: (07)50002917
email: tindaleridgedental@quillpost.com
http://tindaleridgedental.com/

Logo Text

Logo styles of interest
Abstract Logo
Requirements
Must have
• Vertical, Vibrant but Professional, Rounded Edges, Logo on front and back of card (different colours on each side)
Nice to have
• One side completely blue (not sure what shade) with logo and moto on bottom
Other side white, with blue or different coloured logo with details in black and silver?
Logo should show half circle with 1 end as arrow symbolizing pelican waters canal also a magnifine glass also half circled with 1 end as arrow. Any other ideas are welcome.
Should not have
• A tooth. A smile. Toothbrush or Toothpaste. Cornered edges.

```html
<!DOCTYPE html>
<html lang="en">
<head>
<meta charset="utf-8">
<title>Tindale Ridge Dental Surgery – Business Card</title>
<link rel="stylesheet" href="https://fonts.googleapis.com/css2?family=Alegreya+Sans:wght@500&family=Arimo:wght@400;700&display=swap">
<style>
  :root {
    --stage: #d9dbde;
    --card-white: #ffffff;
    --card-mist: #eef0f2;
    --navy: #0e2c47;
    --navy-deep: #061a2c;
    --gold: #94782f;
    --gold-bright: #b39236;
    --ink: #1c1c1c;
    --silver: #c9cfd6;
  }
  * { margin: 0; padding: 0; box-sizing: border-box; }
  html, body { width: 1200px; height: 900px; overflow: hidden; }
  body {
    background: var(--stage);
    position: relative;
    font-family: "Arimo", Arial, sans-serif;
  }
  .card {
    position: absolute;
    top: 112px;
    width: 358px;
    height: 636px;
    border-radius: 18px;
    overflow: hidden;
  }
  .card--front {
    left: 230px;
    background: linear-gradient(180deg, var(--card-white) 0%, var(--card-white) 70%, var(--card-mist) 100%);
    text-align: center;
    color: var(--ink);
  }
  .card--back {
    left: 622px;
    background: radial-gradient(circle at 40% 30%, #123757 0%, var(--navy) 45%, var(--navy-deep) 100%);
  }
  .brand-dot {
    position: absolute;
    left: 149px; top: 48px;
    width: 60px; height: 60px;
    border-radius: 50%;
    background: var(--gold);
  }
  .practice-name {
    position: absolute; top: 122px; left: 0; right: 0;
    font-family: "Alegreya Sans", "Trebuchet MS", sans-serif;
    font-weight: 500;
    font-size: 24px;
    color: var(--gold);
  }
  .motto {
    position: absolute; top: 162px; left: 0; right: 0;
    font-family: "Alegreya Sans", "Trebuchet MS", sans-serif;
    font-weight: 500;
    font-size: 17px;
    color: var(--gold-bright);
  }
  .dentist-name {
    position: absolute; top: 235px; left: 0; right: 0;
    font-size: 23px; letter-spacing: 2px;
  }
  .dentist-role {
    position: absolute; top: 268px; left: 0; right: 0;
    font-size: 16px; letter-spacing: 1px;
  }
  .credentials {
    position: absolute; top: 298px; left: 0; right: 0;
    font-size: 13px;
  }
  .contacts {
    position: absolute; top: 361px; left: 0; right: 0;
    font-size: 16px; letter-spacing: 1.2px; line-height: 24px;
    list-style: none;
  }
  .address-band {
    position: absolute; left: 0; right: 0; bottom: 0;
    height: 128px;
    background: var(--navy);
    color: var(--silver);
    text-align: left;
    padding: 17px 0 0 18px;
    font-size: 17px; letter-spacing: 1.3px; line-height: 23.5px;
    font-style: normal;
  }
  .back-art { position: absolute; inset: 0; }
</style>
</head>
<body>
  <section class="card card--front">
    <span class="brand-dot"></span>
    <h1 class="practice-name">Tindale Ridge Dental Surgery</h1>
    <p class="motto">Family, Cosmetic, Preventive</p>
    <p class="dentist-name">Dr. Owen Castrey</p>
    <p class="dentist-role">Dental Surgeon</p>
    <p class="credentials">BDS (Adel) FAE FADI FICD FPFA</p>
    <ul class="contacts">
      <li>P: (07)50001846</li>
      <li>F: (07)50002917</li>
      <li>E: tindaleridgedental@quillpost.com</li>
      <li>W: tindaleridgedental.com</li>
    </ul>
    <address class="address-band">
      Shop 7<br>
      Tindale Ridge Shopping Village<br>
      28 Tindale Ridge Boulevard<br>
      Tindale Ridge, Tasmania 7250
    </address>
  </section>

  <section class="card card--back">
    <svg class="back-art" width="358" height="636" viewBox="0 0 358 636">
      <defs>
        <path id="motto-arc" d="M 48 533 A 235 235 0 0 1 283 298"/>
      </defs>
      <text font-family="Arimo, Arial, sans-serif" font-weight="700" font-size="21" fill="#e8ecf0">
        <textPath href="#motto-arc" textLength="350" lengthAdjust="spacing">Family, Cosmestic, Preventive</textPath>
      </text>
      <circle class="back-dot" cx="306" cy="540" r="22" fill="#94782f"/>
      <text x="330" y="588" text-anchor="end" font-family="Alegreya Sans, sans-serif" font-weight="500" font-size="22" fill="#c9cfd6">Tindale Ridge</text>
      <text x="330" y="614" text-anchor="end" font-family="Alegreya Sans, sans-serif" font-weight="500" font-size="22" fill="#c9cfd6">Dental Surgery</text>
    </svg>
  </section>
</body>
</html>
```